Web design for Modeling agency

We are looking for re-designing our modeling agency website.
Current website: brisamodels.com our competitor: QRTmodels.com
http://ravonmodel.fr/
https://www.dunforthmanagement.com/models/
https://www.hendra-models.de
https://www.fennmanagement.co.uk
https://www.vantrimodel.com
https://www.brackenfordmodels.com

Target Market(s)

modeling agency

Industry/Entity Type

modeling agency

Number of Pages Required

5+ page

Font styles to use
Other font styles liked:
• base on logo guidline

Requirements
Nice to have
• current website: brisamodels.com our competitor: QRTmodels.com

```html
<!DOCTYPE html>
<html lang="en">
<head>
<meta charset="utf-8">
<title>Brisa Models</title>
<link rel="stylesheet" href="https://fonts.googleapis.com/css2?family=Cormorant+Garamond:wght@400;500&family=Poppins:wght@300;400;500;600&display=swap">
<style>
:root{
  --accent:#b59a7f;
  --accent-dark:#a88b6f;
  --text:#333;
  --muted:#777;
  --line:#e2e2e2;
  --footer:#4b4b4b;
  --white:#fff;
}
*{box-sizing:border-box;margin:0;padding:0}
html,body{width:1200px;height:4087px;overflow:hidden;background:var(--white)}
body{position:relative;font-family:"Poppins",sans-serif;color:var(--text)}
.serif{font-family:"Cormorant Garamond",serif}
.abs{position:absolute}

/* header */
.logo{position:absolute;left:0;width:1200px;top:12px;text-align:center;color:var(--accent)}
.logo .name{font-family:"Cormorant Garamond",serif;font-size:44px;line-height:44px;letter-spacing:1px}
.logo .sub{font-family:"Poppins",sans-serif;font-size:13px;color:#555;letter-spacing:1px;margin-top:2px}
.nav{position:absolute;top:96px;left:18px;width:1164px;display:flex;align-items:center;justify-content:space-between;font-size:11px;color:#444;text-transform:uppercase}
.nav .active{color:var(--accent);border-bottom:1px solid var(--accent);padding-bottom:2px}
.nav svg{display:block}

/* hero */
.hero{position:absolute;top:127px;left:0;width:1200px;height:565px;background:linear-gradient(90deg,#6e3c49 0%,#8a5a63 50%,#6a3a46 100%);overflow:hidden}
.hero .word{position:absolute;left:0;width:1200px;top:140px;text-align:center;font-family:"Cormorant Garamond",serif;font-size:300px;line-height:270px;color:#b79ea1;letter-spacing:10px}
.hero .figure{position:absolute;left:390px;top:0;width:420px;height:565px;background:linear-gradient(180deg,#cfb7a9,#e8ddd6 60%,#d8c9c4)}
.hero .caption{position:absolute;left:110px;top:505px;color:#c9a98f}
.hero .caption b{display:block;font-family:"Cormorant Garamond",serif;font-weight:400;font-size:22px}
.hero .caption span{display:block;font-size:10px;color:#eee;margin-left:62px;letter-spacing:1px}
.hero .arrow{position:absolute;top:262px}

/* category tiles */
.tile{position:absolute;top:706px;width:223px;height:294px;border:1px solid var(--line)}
.tile .ph{height:253px}
.tile .lbl{height:40px;line-height:40px;text-align:center;font-family:"Cormorant Garamond",serif;font-size:15px;color:#444;text-transform:uppercase;letter-spacing:.5px}
.tile.hover .lbl{color:var(--accent)}

.section-title{position:absolute;left:0;width:1200px;text-align:center;font-family:"Cormorant Garamond",serif;font-size:46px;color:var(--accent);letter-spacing:1px}
.section-title i{display:inline-block;width:40px;height:1px;background:var(--accent);vertical-align:middle;margin:0 14px}

/* videos */
.video-main{position:absolute;left:110px;top:1133px;width:666px;height:433px;background:linear-gradient(180deg,#d4d4d4,#c6c6c6)}
.play{position:absolute;border-radius:50%;background:rgba(60,60,60,.6);border:2px solid #fff}
.video-item{position:absolute;left:795px;width:294px;height:94px;border:1px solid var(--line)}
.video-item .th{position:absolute;left:0;top:0;width:121px;height:92px}
.video-item .tx{position:absolute;left:141px;top:18px;font-size:9px;color:#444;text-transform:uppercase}
.video-item .tx b{display:block;font-family:"Cormorant Garamond",serif;font-weight:400;font-size:13px;line-height:19px;color:var(--accent);margin-top:6px}
.btn{position:absolute;background:var(--accent);color:#fff;font-size:11px;font-weight:500;text-align:center;letter-spacing:.5px}

/* news */
.card{position:absolute;width:275px}
.card .ph{height:319px}
.card .meta{font-size:10px;color:#555;margin-top:19px}
.card .title{font-family:"Cormorant Garamond",serif;font-size:15px;color:#222;margin-top:6px;text-transform:uppercase}
.card .share{display:flex;justify-content:space-around;align-items:center;border-top:1px solid var(--line);border-bottom:1px solid var(--line);height:31px;margin-top:12px}
.card .share .dot{width:7px;height:7px;border-radius:50%;background:#c4a893}

/* models */
.model{position:absolute;top:3328px;width:223px}
.model .ph{height:267px;position:relative}
.model .nm{text-align:center;font-family:"Cormorant Garamond",serif;font-size:15px;margin-top:17px;text-transform:uppercase;color:#333}
.model.hover .nm{color:var(--accent)}
.overlay{position:absolute;left:12px;top:12px;right:12px;bottom:0;background:rgba(181,154,127,.8)}

/* footer */
.footer{position:absolute;left:0;top:3694px;width:1200px;height:393px;background:var(--footer);color:#eee}
.footer h4{font-family:"Cormorant Garamond",serif;font-weight:500;font-size:18px;letter-spacing:1px;color:#fff;text-transform:uppercase}
.contact{position:absolute;left:211px;top:70px;width:240px}
.contact .row{display:flex;align-items:flex-start;gap:12px;font-size:10px;line-height:16px;margin-top:15px}
.contact .row.strong{font-weight:600}
.contact svg{flex:none;margin-top:1px}
.flogo{position:absolute;left:503px;top:94px;width:200px;text-align:center;color:var(--accent)}
.flogo .name{font-family:"Cormorant Garamond",serif;font-size:44px;line-height:44px}
.flogo .sub{font-size:15px;color:#eee;margin-top:2px}
.flogo .social{display:flex;justify-content:center;gap:10px;margin-top:14px}
.flogo .social span{width:31px;height:31px;border-radius:50%;background:var(--accent)}
.links{position:absolute;left:871px;top:70px}
.links ul{list-style:none;margin-top:14px}
.links li{font-size:10px;line-height:24.5px}
.copy{position:absolute;left:0;bottom:0;width:1200px;height:48px;border-top:1px solid #5c5c5c;text-align:center;line-height:44px;font-size:9px;color:#ccc;letter-spacing:.3px}
</style>
</head>
<body>

<header>
  <div class="logo"><div class="name">BRISA</div><div class="sub">MODELS</div></div>
  <nav class="nav">
    <svg width="22" height="14" viewBox="0 0 22 14"><path d="M0 1h22M0 7h22M0 13h22" stroke="#b59a7f" stroke-width="2"/></svg>
    <span class="active">Home</span>
    <span>About us</span>
    <span>Men ⌄</span>
    <span>Women ⌄</span>
    <span>Development ⌄</span>
    <span>Talent</span>
    <span>News</span>
    <span>Contact</span>
    <svg width="18" height="18" viewBox="0 0 18 18"><circle cx="7.5" cy="7.5" r="6" fill="none" stroke="#b59a7f" stroke-width="1.6"/><path d="M12 12l5 5" stroke="#b59a7f" stroke-width="1.8"/></svg>
  </nav>
</header>

<section class="hero">
  <div class="word">BRISA</div>
  <div class="figure" role="img" aria-label="Model in a white knit sweater and black hat seated on a white block"></div>
  <div class="caption"><b>NADIA VELLE</b><span>— IN TOWN</span></div>
  <svg class="arrow" style="left:45px" width="20" height="38" viewBox="0 0 20 38"><path d="M18 2L3 19l15 17" fill="none" stroke="#fff" stroke-width="1.5"/></svg>
  <svg class="arrow" style="left:1135px" width="20" height="38" viewBox="0 0 20 38"><path d="M2 2l15 17L2 36" fill="none" stroke="#fff" stroke-width="1.5"/></svg>
</section>

<section class="categories">
  <div class="tile" style="left:13px"><div class="ph" role="img" aria-label="Male model in black tee before a striped wall" style="background:linear-gradient(90deg,#222,#ddd 20%,#222 40%,#eee 60%,#222 80%,#ccc)"></div><div class="lbl">Men</div></div>
  <div class="tile" style="left:250px"><div class="ph" role="img" aria-label="Female model in floral dress by a red shuttered wall" style="background:linear-gradient(160deg,#8a3a4a,#c89aa0 55%,#7b3040)"></div><div class="lbl">Women</div></div>
  <div class="tile hover" style="left:488px"><div class="ph" role="img" aria-label="Young male model in grey blazer on a city street" style="background:linear-gradient(180deg,#cfd3d6,#8d8e90 70%,#5a5c60)"></div><div class="lbl">Men Devlopment</div></div>
  <div class="tile" style="left:725px"><div class="ph" role="img" aria-label="Red-haired female model in olive dotted dress" style="background:linear-gradient(180deg,#d9d2a8,#6d6a3c 60%,#4b4a2c)"></div><div class="lbl">Women Devlopment</div></div>
  <div class="tile" style="left:963px"><div class="ph" role="img" aria-label="Two models posing together in knitwear" style="background:linear-gradient(90deg,#d7dadf,#b9c0c8 45%,#6e2f35 70%,#d6d7da)"></div><div class="lbl">Talent</div></div>
</section>

<h2 class="section-title" style="top:1058px"><i></i>OUR VIDEOS<i></i></h2>

<section class="videos">
  <div class="video-main" role="img" aria-label="Video still of a model in a brown coat seated on a white block">
    <svg class="abs" style="left:306px;top:190px" width="54" height="54" viewBox="0 0 54 54"><circle cx="27" cy="27" r="25" fill="rgba(70,70,70,.55)" stroke="#fff" stroke-width="2.5"/><path d="M21 16l17 11-17 11z" fill="#fff"/></svg>
  </div>
  <div class="video-item" style="top:1133px"><div class="th" role="img" aria-label="Two models in black" style="background:linear-gradient(90deg,#8a8c90,#d4d6d8 50%,#3aa1a8)"></div><div class="tx">Brisa original<b>TESSA MORROW &amp;<br>JORY CALDER 2021</b></div></div>
  <div class="video-item" style="top:1246px"><div class="th" role="img" aria-label="Model seated on a block" style="background:linear-gradient(180deg,#e4e4e4,#b7a49a)"></div><div class="tx">Brisa original<b>MINA CORRAL ASHBY<br>F/W 2021</b></div></div>
  <div class="video-item" style="top:1360px"><div class="th" role="img" aria-label="Male model in black" style="background:linear-gradient(90deg,#f2f2f2,#333 60%,#1e1e1e)"></div><div class="tx">Brisa original<b>DARIO FENWICK<br>F/W 2021</b></div></div>
  <div class="video-item" style="top:1473px"><div class="th" role="img" aria-label="Model against a violet backdrop" style="background:linear-gradient(90deg,#5a4fd0,#8b7fe0 50%,#4a3fb8)"></div><div class="tx">Brisa original<b>GETTING TO KNOW<br>ILSE HARROW</b></div></div>
  <div class="btn" style="left:527px;top:1600px;width:146px;height:40px;line-height:40px">VIEW ALL</div>
</section>

<h2 class="section-title" style="top:1698px"><i></i>OUR NEWS<i></i></h2>

<section class="news">
  <article class="card" style="left:19px;top:1774px"><div class="ph" role="img" aria-label="Male model in leather jacket by a red wall" style="background:linear-gradient(180deg,#d8504b,#2a2a2a 70%,#5a3a2a)"></div><div class="meta">22—October—2021 &nbsp;|&nbsp; MEN</div><div class="title">Selin Arden | Perfect F/W 2021</div><div class="share"><span class="dot"></span><span class="dot"></span><span class="dot"></span><span class="dot"></span><svg width="13" height="9" viewBox="0 0 13 9"><rect width="13" height="9" fill="#c4a893"/><path d="M0 0l6.5 5L13 0" fill="none" stroke="#fff"/></svg></div></article>
  <article class="card" style="left:314px;top:1774px"><div class="ph" role="img" aria-label="Female model in printed skirt and orange jacket" style="background:linear-gradient(180deg,#6d9ab0,#d77040 50%,#8cbf5e)"></div><div class="meta">21—October—2021 &nbsp;|&nbsp; WOMEN</div><div class="title">Veda Lorne | Another F/W 2021</div><div class="share"><span class="dot"></span><span class="dot"></span><span class="dot"></span><span class="dot"></span><svg width="13" height="9" viewBox="0 0 13 9"><rect width="13" height="9" fill="#c4a893"/><path d="M0 0l6.5 5L13 0" fill="none" stroke="#fff"/></svg></div></article>
  <article class="card" style="left:610px;top:1774px"><div class="ph" role="img" aria-label="Female model in red gown on a cobbled street" style="background:linear-gradient(180deg,#e8e2d8,#b8202a 50%,#8f8a84)"></div><div class="meta">19—October—2021 &nbsp;|&nbsp; WOMEN</div><div class="title">Selin Arden | Perfect F/W 2021</div><div class="share"><span class="dot"></span><span class="dot"></span><span class="dot"></span><span class="dot"></span><svg width="13" height="9" viewBox="0 0 13 9"><rect width="13" height="9" fill="#c4a893"/><path d="M0 0l6.5 5L13 0" fill="none" stroke="#fff"/></svg></div></article>
  <article class="card" style="left:906px;top:1774px"><div class="ph" role="img" aria-label="Female model in sheer dress and straw hat by a lilac wall" style="background:linear-gradient(180deg,#d9c8e0,#7d6a80 60%,#cdb8d6)"></div><div class="meta">19—October—2021 &nbsp;|&nbsp; WOMEN</div><div class="title">Selin Arden | Perfect F/W 2021</div><div class="share"><span class="dot"></span><span class="dot"></span><span class="dot"></span><span class="dot"></span><svg width="13" height="9" viewBox="0 0 13 9"><rect width="13" height="9" fill="#c4a893"/><path d="M0 0l6.5 5L13 0" fill="none" stroke="#fff"/></svg></div></article>

  <article class="card" style="left:19px;top:2228px"><div class="ph" role="img" aria-label="Female model in striped trousers among green leaves" style="background:linear-gradient(90deg,#3f7a3a,#e6e6e6 60%,#bdbdbd)"></div><div class="meta">15—October—2021 &nbsp;|&nbsp; WOMEN</div><div class="title">Selin Arden | Perfect F/W 2021</div><div class="share"><span class="dot"></span><span class="dot"></span><span class="dot"></span><span class="dot"></span><svg width="13" height="9" viewBox="0 0 13 9"><rect width="13" height="9" fill="#c4a893"/><path d="M0 0l6.5 5L13 0" fill="none" stroke="#fff"/></svg></div></article>
  <article class="card" style="left:314px;top:2228px"><div class="ph" role="img" aria-label="Male model in brown jacket seated on wooden pallets" style="background:linear-gradient(180deg,#4a4a4a,#7a4a30 50%,#8a6a4a)"></div><div class="meta">14—October—2021 &nbsp;|&nbsp; MEN</div><div class="title">Veda Lorne | Another F/W 2021</div><div class="share"><span class="dot"></span><span class="dot"></span><span class="dot"></span><span class="dot"></span><svg width="13" height="9" viewBox="0 0 13 9"><rect width="13" height="9" fill="#c4a893"/><path d="M0 0l6.5 5L13 0" fill="none" stroke="#fff"/></svg></div></article>
  <article class="card" style="left:610px;top:2228px"><div class="ph" role="img" aria-label="Male model in orange coat and hat" style="background:linear-gradient(180deg,#e6e6e6,#e08a5a 55%,#d8d8d8)"></div><div class="meta">13—October—2021 &nbsp;|&nbsp; MEN</div><div class="title">Selin Arden | Perfect F/W 2021</div><div class="share"><span class="dot"></span><span class="dot"></span><span class="dot"></span><span class="dot"></span><svg width="13" height="9" viewBox="0 0 13 9"><rect width="13" height="9" fill="#c4a893"/><path d="M0 0l6.5 5L13 0" fill="none" stroke="#fff"/></svg></div></article>
  <article class="card" style="left:906px;top:2228px"><div class="ph" role="img" aria-label="Blonde female model in knit sweater and plaid coat" style="background:linear-gradient(180deg,#3a3a3a,#d8cfc4 50%,#6a5040)"></div><div class="meta">10—October—2021 &nbsp;|&nbsp; WOMEN</div><div class="title">Selin Arden | Perfect F/W 2021</div><div class="share"><span class="dot"></span><span class="dot"></span><span class="dot"></span><span class="dot"></span><svg width="13" height="9" viewBox="0 0 13 9"><rect width="13" height="9" fill="#c4a893"/><path d="M0 0l6.5 5L13 0" fill="none" stroke="#fff"/></svg></div></article>

  <article class="card" style="left:19px;top:2682px"><div class="ph" role="img" aria-label="Female model in black wrap top against violet wall" style="background:linear-gradient(90deg,#9b86c8,#1e1e1e 50%,#9b86c8)"></div><div class="meta">10—October—2021 &nbsp;|&nbsp; WOMEN</div><div class="title">Selin Arden | Perfect F/W 2021</div><div class="share"><span class="dot"></span><span class="dot"></span><span class="dot"></span><span class="dot"></span><svg width="13" height="9" viewBox="0 0 13 9"><rect width="13" height="9" fill="#c4a893"/><path d="M0 0l6.5 5L13 0" fill="none" stroke="#fff"/></svg></div></article>
  <article class="card" style="left:314px;top:2682px"><div class="ph" role="img" aria-label="Female model in lace blouse and rust skirt against blue wall" style="background:linear-gradient(180deg,#a9c6cf,#f0ece6 45%,#b4583a 70%,#a9c6cf)"></div><div class="meta">09—October—2021 &nbsp;|&nbsp; WOMEN</div><div class="title">Veda Lorne | Another F/W 2021</div><div class="share"><span class="dot"></span><span class="dot"></span><span class="dot"></span><span class="dot"></span><svg width="13" height="9" viewBox="0 0 13 9"><rect width="13" height="9" fill="#c4a893"/><path d="M0 0l6.5 5L13 0" fill="none" stroke="#fff"/></svg></div></article>
  <article class="card" style="left:610px;top:2682px"><div class="ph" role="img" aria-label="Female model in swimwear by the sea" style="background:linear-gradient(180deg,#8ab0bf,#c49a7e 50%,#2e5a78)"></div><div class="meta">05—October—2021 &nbsp;|&nbsp; WOMEN</div><div class="title">Selin Arden | Perfect F/W 2021</div><div class="share"><span class="dot"></span><span class="dot"></span><span class="dot"></span><span class="dot"></span><svg width="13" height="9" viewBox="0 0 13 9"><rect width="13" height="9" fill="#c4a893"/><path d="M0 0l6.5 5L13 0" fill="none" stroke="#fff"/></svg></div></article>
  <article class="card" style="left:906px;top:2682px"><div class="ph" role="img" aria-label="Male model in white tee beside a black car" style="background:linear-gradient(180deg,#e4e6e8,#f2f2f2 40%,#1f1f22 70%,#9a9a9a)"></div><div class="meta">05—October—2021 &nbsp;|&nbsp; MEN</div><div class="title">Selin Arden | Perfect F/W 2021</div><div class="share"><span class="dot"></span><span class="dot"></span><span class="dot"></span><span class="dot"></span><svg width="13" height="9" viewBox="0 0 13 9"><rect width="13" height="9" fill="#c4a893"/><path d="M0 0l6.5 5L13 0" fill="none" stroke="#fff"/></svg></div></article>

  <div class="btn" style="left:516px;top:3141px;width:166px;height:40px;line-height:40px">SHOW MORE</div>
</section>

<h2 class="section-title" style="top:3251px"><i></i>FAMOUS MODELS<i></i></h2>

<section class="models">
  <div class="model" style="left:13px"><div class="ph" role="img" aria-label="Male model in black turtleneck" style="background:linear-gradient(180deg,#cfcfcf,#2a2a2a 55%,#1f1f1f)"></div><div class="nm">Teodor</div></div>
  <div class="model" style="left:250px"><div class="ph" role="img" aria-label="Female model in green jacket and black hat" style="background:linear-gradient(180deg,#8a8680,#2f9a4a 55%,#6a6a6a)"></div><div class="nm">Marta L.</div></div>
  <div class="model hover" style="left:488px"><div class="ph" role="img" aria-label="Female model in a camel coat" style="background:linear-gradient(180deg,#6c6a66,#b8a690)"><div class="overlay"></div><svg class="abs" style="left:101px;top:124px" width="20" height="20" viewBox="0 0 20 20"><circle cx="10" cy="10" r="8" fill="none" stroke="#fff" stroke-width="1.6"/></svg></div><div class="nm">Yana K.</div></div>
  <div class="model" style="left:725px"><div class="ph" role="img" aria-label="Male model in camel coat by the waterfront" style="background:linear-gradient(180deg,#b9c8d4,#8a6a50 55%,#e4e4e4)"></div><div class="nm">Emil</div></div>
  <div class="model" style="left:963px"><div class="ph" role="img" aria-label="Female model in red lace dress" style="background:linear-gradient(180deg,#e8e2dc,#d8404a 55%,#c0b8b0)"></div><div class="nm">Odessa</div></div>
</section>

<footer class="footer">
  <div class="contact">
    <h4>Contact Us</h4>
    <div class="row"><svg width="14" height="16" viewBox="0 0 14 16"><path d="M7 15s5.5-5.5 5.5-9A5.5 5.5 0 0 0 1.5 6c0 3.5 5.5 9 5.5 9z" fill="none" stroke="#b59a7f" stroke-width="1.5"/><circle cx="7" cy="6" r="2" fill="#b59a7f"/></svg><span>Unit 48, Floor 9th, C Blok, Larkmoor<br>building, Eskin Local, Dervan,<br>Istanbul, Turkey</span></div>
    <div class="row strong"><svg width="14" height="13" viewBox="0 0 14 13"><path d="M1 4c0-2 12-2 12 0v1H10V3.5H4V5H1z" fill="#b59a7f"/><rect x="2" y="6" width="10" height="6" rx="1" fill="#b59a7f"/></svg><span>(+44) 700 555 01 48</span></div>
    <div class="row strong"><svg width="14" height="14" viewBox="0 0 14 14"><path d="M3 1l2.5 3-1.5 1.5c.8 1.8 2.2 3.2 4 4L9.5 8 12.5 10.5 11 13C5.5 12.5 1.5 8.5 1 3z" fill="none" stroke="#b59a7f" stroke-width="1.4"/></svg><span>(+90) 500 555 12 34</span></div>
    <div class="row"><svg width="15" height="11" viewBox="0 0 15 11"><rect width="15" height="11" fill="#b59a7f"/><path d="M0 0l7.5 6L15 0" fill="none" stroke="#4b4b4b" stroke-width="1.2"/></svg><span>booker@brisamodels.com</span></div>
  </div>
  <div class="flogo">
    <div class="name">BRISA</div>
    <div class="sub">MODELS</div>
    <div class="social"><span></span><span></span><span></span></div>
  </div>
  <div class="links">
    <h4>Quick Links</h4>
    <ul><li>Home</li><li>About Us</li><li>Men</li><li>Women</li><li>Devlopment</li><li>Talent</li><li>News</li><li>Contact</li></ul>
  </div>
  <div class="copy">COPYRIGHT ©2021 BRISA MODELS. ALL RIGHTS RESERVED.</div>
</footer>

</body>
</html>
```